A Book Cover For a Book Called "Tamsire"

Attached are two files for the ISBN bar graph for the print version of the cover! Same image, just two different formats.
Updates

Project Deadline Extended Reason: We'd like to see a few more designs, and work with a few of the designs already submitted. Added Tuesday, October 24, 2017

Target Market(s)

young adult female, parents

Colors

Designer to choose colors to be used in the design.

```html
<!DOCTYPE html>
<html lang="en">
<head>
<meta charset="utf-8">
<title>Tamsire – A Memoir</title>
<link href="https://fonts.googleapis.com/css2?family=Great+Vibes&family=Alegreya+Sans:wght@400;500&display=swap" rel="stylesheet">
<style>
  :root {
    --page-bg: #ffffff;
    --cover-edge: #26313f;
    --cover-mid: #3d4a5d;
    --cover-glow: #c7cedc;
    --title-ink: #dfe2ef;
    --subtitle-ink: #eceff6;
    --author-ink: #e4e7f0;
    --rule: rgba(235, 240, 250, 0.75);
    --art-warm: #e07a5f;
    --art-pale: #d9dde6;
    --art-water: #56657a;
  }
  * { margin: 0; padding: 0; box-sizing: border-box; }
  html, body {
    width: 960px;
    height: 1200px;
    overflow: hidden;
    background: var(--page-bg);
  }
  .canvas {
    position: relative;
    width: 960px;
    height: 1200px;
  }
  .cover {
    position: absolute;
    left: 110px;
    top: 20px;
    width: 740px;
    height: 1160px;
    overflow: hidden;
    background:
      radial-gradient(ellipse 62% 42% at 50% 46%, var(--cover-glow) 0%, #8e9aae 30%, var(--cover-mid) 68%, var(--cover-edge) 100%);
  }
  .title {
    position: absolute;
    top: 90px;
    left: 0;
    width: 100%;
    text-align: center;
    font-family: "Great Vibes", cursive;
    font-size: 190px;
    line-height: 1;
    color: var(--title-ink);
    text-shadow: 3px 4px 5px rgba(20, 28, 40, 0.55);
  }
  .subtitle {
    position: absolute;
    top: 445px;
    left: 0;
    width: 100%;
    text-align: center;
    font-family: "Alegreya Sans", sans-serif;
    font-size: 58px;
    font-weight: 500;
    color: var(--subtitle-ink);
    text-shadow: 2px 3px 3px rgba(30, 38, 52, 0.6);
  }
  .subtitle-rule {
    position: absolute;
    top: 540px;
    left: 160px;
    width: 420px;
    height: 2px;
    background: linear-gradient(90deg, transparent, var(--rule) 50%, transparent);
  }
  .cover-art {
    position: absolute;
    top: 720px;
    left: 110px;
    width: 520px;
    height: 240px;
  }
  .authors {
    position: absolute;
    bottom: 62px;
    left: 0;
    width: 100%;
    text-align: center;
    font-family: "Alegreya Sans", sans-serif;
    font-size: 46px;
    color: var(--author-ink);
    text-shadow: 2px 2px 3px rgba(15, 22, 32, 0.6);
  }
</style>
</head>
<body>
  <main class="canvas">
    <section class="cover">
      <h1 class="title">Tamsire</h1>
      <p class="subtitle">A Memoir</p>
      <div class="subtitle-rule"></div>
      <svg class="cover-art" viewBox="0 0 520 240" role="img" aria-label="Bouquet of coral roses beside a pair of white pointe shoes resting on rippling water">
        <defs>
          <radialGradient id="water" cx="50%" cy="50%" r="50%">
            <stop offset="0%" stop-color="var(--art-water)" stop-opacity="0.9"/>
            <stop offset="100%" stop-color="var(--art-water)" stop-opacity="0"/>
          </radialGradient>
          <linearGradient id="still" x1="0" y1="0" x2="1" y2="0">
            <stop offset="0%" stop-color="var(--art-warm)"/>
            <stop offset="45%" stop-color="#c6768a"/>
            <stop offset="60%" stop-color="var(--art-pale)"/>
            <stop offset="100%" stop-color="#b9bfcc"/>
          </linearGradient>
        </defs>
        <ellipse cx="260" cy="190" rx="260" ry="50" fill="url(#water)"/>
        <rect x="90" y="20" width="340" height="170" rx="80" fill="url(#still)" opacity="0.85"/>
      </svg>
      <p class="authors">Sadie Morrow &amp; Nora Whitley</p>
    </section>
  </main>
</body>
</html>
```